Store Fixture business needs a buisness card design

We are looking for a business card design for a store fixture company. "QL Store Fixtures" we help small businesses with their start up by providing fixtures required to display their products.
It should have a simple yet innovative design in the front, and a refined look to our company.
We would like our logo, to have one of our products "display cases, clothing rack, mannequins" integrated in the design. And the rest of it just a clean look, which gives our address, store hours, and contact number, etc.
The color scheme as seen in the samples can be changed as long as the goal is achieved.
Industry/Entity Type
Business
Contact Information for Business Card
QL Store Fixtures
4269 Marlowe St.
San Antonio,TX 78217
www.qlstorefixtures.example
qlbx@qlstorefixture.example
(210) 555-0193
M-F: 9-6pm
Sat: 10-3pm

```html
<!DOCTYPE html>
<html lang="en">
<head>
<meta charset="utf-8">
<title>QL Store Fixtures – Business Card</title>
<link rel="stylesheet" href="https://fonts.googleapis.com/css2?family=Lato:wght@400;700&family=Michroma&display=swap">
<style>
  :root {
    --page: #e9e6e1;
    --card-front-top: #626262;
    --card-front-bottom: #3e3e3e;
    --card-back: #0b0b0b;
    --accent: #f2a91d;
    --accent-dark: #c98708;
    --text-light: #f4f4f4;
    --icon-ink: #3a3a3a;
  }
  * { box-sizing: border-box; margin: 0; padding: 0; }
  html, body { width: 1200px; height: 950px; overflow: hidden; }
  body {
    background: var(--page);
    font-family: "Lato", Arial, sans-serif;
    color: var(--text-light);
    display: flex;
    justify-content: center;
    align-items: center;
    gap: 80px;
  }
  .card {
    width: 400px;
    height: 700px;
    border-radius: 6px;
    position: relative;
    overflow: hidden;
    box-shadow: 0 12px 30px rgba(0,0,0,.25);
  }

  /* Front */
  .card-front {
    background: linear-gradient(160deg, var(--card-front-top), var(--card-front-bottom));
    padding: 70px 40px 0 40px;
  }
  .brand {
    display: flex;
    align-items: center;
    justify-content: flex-end;
    gap: 12px;
  }
  .brand-square {
    width: 26px; height: 26px;
    background: var(--accent);
  }
  .brand-name {
    font-family: "Michroma", sans-serif;
    font-size: 22px;
    line-height: 1.2;
    color: var(--text-light);
    text-align: right;
    text-transform: uppercase;
  }
  .contact-list { list-style: none; margin-top: 150px; }
  .contact-item {
    display: flex;
    align-items: center;
    gap: 18px;
    padding: 13px 0;
    border-bottom: 1px solid var(--accent);
    font-size: 17px;
    line-height: 1.3;
  }
  .contact-icon {
    flex: 0 0 26px;
    width: 26px; height: 26px;
    border-radius: 50%;
    background: var(--accent);
    display: flex; align-items: center; justify-content: center;
  }
  .contact-icon svg { width: 14px; height: 14px; }

  /* Back */
  .card-back {
    background: var(--card-back);
    padding: 36px 28px 0 28px;
  }
  .product-grid {
    display: grid;
    grid-template-columns: 1fr 1fr;
    gap: 22px 20px;
  }
  .product-tile { position: relative; height: 160px; }
  .product-photo { width: 100%; height: 130px; }
  .photo-racks { background: linear-gradient(160deg, #ffffff, #d9d9d9); }
  .photo-cases { background: linear-gradient(160deg, #f5f5f5, #b8322e 70%, #8e1e1c); }
  .photo-mannequins { background: linear-gradient(160deg, #6a6a6a, #2e2e2e); }
  .photo-shelving { background: linear-gradient(160deg, #ffffff, #e7d9cc); }
  .product-label {
    position: absolute; left: 0; right: 0; bottom: 0;
    height: 30px;
    background: var(--accent);
    color: #1b1b1b;
    font-size: 14px;
    display: flex; align-items: center; justify-content: center;
  }
  .product-label::after {
    content: "";
    position: absolute; right: 6px; bottom: 6px;
    border-left: 5px solid transparent;
    border-right: 5px solid transparent;
    border-bottom: 7px solid #1b1b1b;
  }
  .back-name {
    margin-top: 44px;
    font-family: "Michroma", sans-serif;
    font-size: 30px;
    line-height: 1.25;
    text-align: center;
    text-transform: uppercase;
    color: var(--text-light);
  }
  .social-row {
    display: flex; align-items: center; gap: 8px;
    margin-top: 22px;
  }
  .social-row .rule { flex: 1; height: 1px; background: var(--accent); }
  .social-dot { width: 22px; height: 22px; border-radius: 50%; background: var(--accent); }
  .hours {
    margin-top: 16px;
    text-align: center;
    font-size: 16px;
    color: var(--text-light);
  }
  .hours .sep { margin: 0 10px; color: var(--accent); }
</style>
</head>
<body>

  <section class="card card-front" aria-label="Business card front">
    <div class="brand">
      <span class="brand-square"></span>
      <span class="brand-name">QL Store<br>Fixtures</span>
    </div>

    <ul class="contact-list">
      <li class="contact-item">
        <span class="contact-icon"><svg viewBox="0 0 14 14"><path d="M7 1a4 4 0 0 0-4 4c0 3 4 8 4 8s4-5 4-8a4 4 0 0 0-4-4zm0 5.5A1.5 1.5 0 1 1 7 3.5a1.5 1.5 0 0 1 0 3z" fill="var(--icon-ink)"/></svg></span>
        <span>4269 Marlowe St.<br>San Antonio, TX 78217</span>
      </li>
      <li class="contact-item">
        <span class="contact-icon"><svg viewBox="0 0 14 14"><path d="M3.5 1.5l2 2.5-1.2 1.3a7 7 0 0 0 4.4 4.4L10 8.5l2.5 2-1 2A10 10 0 0 1 1.5 2.5z" fill="var(--icon-ink)"/></svg></span>
        <span>(210) 555-0193</span>
      </li>
      <li class="contact-item">
        <span class="contact-icon"><svg viewBox="0 0 14 14"><rect x="1.5" y="3" width="11" height="8" fill="var(--icon-ink)"/><path d="M1.5 3l5.5 4.5L12.5 3" stroke="var(--accent)" stroke-width="1" fill="none"/></svg></span>
        <span>qlbx@qlstorefixture.example</span>
      </li>
      <li class="contact-item">
        <span class="contact-icon"><svg viewBox="0 0 14 14"><circle cx="7" cy="7" r="5.5" fill="none" stroke="var(--icon-ink)" stroke-width="1.3"/><path d="M1.5 7h11M7 1.5c2.5 3 2.5 8 0 11M7 1.5c-2.5 3-2.5 8 0 11" fill="none" stroke="var(--icon-ink)" stroke-width="1"/></svg></span>
        <span>www.qlstorefixtures.example</span>
      </li>
    </ul>
  </section>

  <section class="card card-back" aria-label="Business card back">
    <div class="product-grid">
      <div class="product-tile">
        <div class="product-photo photo-racks" role="img" aria-label="Photo of a chrome clothing rack"></div>
        <div class="product-label">Clothing racks</div>
      </div>
      <div class="product-tile">
        <div class="product-photo photo-cases" role="img" aria-label="Photo of a glass display case with red frame"></div>
        <div class="product-label">Display cases</div>
      </div>
      <div class="product-tile">
        <div class="product-photo photo-mannequins" role="img" aria-label="Photo of a standing mannequin"></div>
        <div class="product-label">Mannequins</div>
      </div>
      <div class="product-tile">
        <div class="product-photo photo-shelving" role="img" aria-label="Photo of white gondola shelving unit"></div>
        <div class="product-label">Gondola shelving</div>
      </div>
    </div>

    <div class="back-name">QL Store<br>Fixtures</div>

    <div class="social-row">
      <span class="rule"></span>
      <span class="social-dot"></span>
      <span class="social-dot"></span>
      <span class="social-dot"></span>
      <span class="rule"></span>
    </div>

    <p class="hours">Mon-Fri: 9-6pm<span class="sep">|</span>Sat: 10-3pm</p>
  </section>

</body>
</html>
```